Design website banners for teeth whitening clinic based on clear examples we have provided.

Hi All,

Thank for for looking at my design project. I am looking forward to seeing your work and providing some feedback.

We are a teeth whitening company called Gleamora Dental and we are having our website updated as we speak. For the new site we are in need of several banners

I have attached some banners which we love and we would love to keep the same style/theme for our banners.

We like the blue fading squares from the edges of the banners so we would like to keep this as a consistent theme across all banners.

HOMEPAGE BANNERS to be the following dimensions: 1920 width x 800 height

Banner1.1 ( Varnek More Info):
Headline Text: Worlds most advanced, award winning whitening technology
Button: Read More
Image: please use picture of Trelwin Varnek whitening machine
Background: Please use photo of someone smiling - white teeth

Banner 1.2 (Varnek Book Now - same as banner 1.1 but with different button) :
Button: Book Now

Banner2.1 (Varnek special1) :
Headline Text: Worlds most advanced whitening technology just got better.
Headline subtext: 1-Hour In chair treatment for just $149! Save $350 -
Button: Book Now
Background: Please use photo of someone smiling - white teeth ( can be same as banner 1)

Banner2.2 (Varnek special2 - same as banner 2.1 just with different price) :
Headline subtext: 1-Hour In chair treatment for just $129! Save $370 -
Button: Book Now

Banner3 ( Whitening pens) :
Headline Text: Any time, any where.
Button: Buy Now
Image: please use images of gleamora dental teeth whitening pens
( Same look, feel and layout to the image attached called Pens Example)
Background: Please use photo of someone smiling - white teeth - can be a couple or anything. Just use judgement what you think looks good.

Banner4 ( Whitening Kits) :
Headline Text: The revolution in home teeth whitening is here
Button: Buy Now
Image: Product images arent ready yet but please leave space for them to be put in later.

SPECIFIC PAGE BANNERS - These do not need images of the actual product in them. These need to be 1600 x 500 size

Banner5 ( Online Store) :
Headline Text: Online Store
Headline Sub text: 48 Hour Express Delivery Nationwide
Background: Just use judgement what you think looks good.

Banner6 ( Whitening Kits ) :
Headline Text: At Home teeth whitening system
(Please see image attached called ' home whitening system' and use this as an example)

Banner7 ( Whitening Pens ) :

There will be 2 more to come.

Target Market(s)

Mostly (70%) Female customers between 20-40 years old who take pride in their personal appearance and dont mind spending money on cosmetic enhancements.

Industry/Entity Type

Clinic

Requirements
Must have
• A very similar look and feel to the banner examples provided and those that can be seen on www.lumidexa.com
• Colour should fit in with logo of www.gleamoradental.co.nz eg: light- medium blue

```html
<!DOCTYPE html>
<html lang="en">
<head>
<meta charset="utf-8">
<title>Banner 4 – Home Whitening Kits</title>
<link rel="stylesheet" href="https://fonts.googleapis.com/css2?family=PT+Sans&family=Source+Sans+3:wght@300;400&display=swap">
<style>
  :root {
    --board-bg: #1b1b1b;
    --board-bg-light: #262626;
    --board-label: #a3a3a3;
    --headline-blue: #2b7cc2;
    --button-top: #2a78c0;
    --button-bottom: #0b4a8f;
    --button-text: #ffffff;
    --product-front: #1f75bb;
    --product-side: #175f9c;
    --banner-white: #f6f9fc;
    --banner-ice: #e3f4fa;
    --banner-blue: #9cc6e6;
    --banner-peach: #ecd6c8;
    --banner-sand: #d8c2a4;
    --photo-hair: #4a362c;
    --photo-skin: #dcae92;
    --photo-sweater: #ece8e3;
  }

  * { margin: 0; padding: 0; box-sizing: border-box; }

  html, body {
    width: 1200px;
    height: 686px;
    overflow: hidden;
  }

  body {
    position: relative;
    background: radial-gradient(ellipse at 50% 40%, var(--board-bg-light), var(--board-bg) 75%);
    font-family: "Source Sans 3", "PT Sans", sans-serif;
  }

  .board-label {
    position: absolute;
    top: 62px;
    left: 0;
    width: 1200px;
    text-align: center;
    font-family: "PT Sans", sans-serif;
    font-size: 34px;
    font-weight: 400;
    color: var(--board-label);
    letter-spacing: 0.2px;
  }

  .banner {
    position: absolute;
    left: 132px;
    top: 146px;
    width: 952px;
    height: 396px;
    overflow: hidden;
    background:
      radial-gradient(ellipse 260px 200px at 280px 170px, var(--banner-white) 0%, rgba(246,249,252,0) 100%),
      radial-gradient(ellipse 220px 160px at 120px 60px, var(--banner-ice) 0%, rgba(227,244,250,0) 100%),
      radial-gradient(ellipse 240px 120px at 230px 400px, var(--banner-blue) 0%, rgba(156,198,230,0) 100%),
      radial-gradient(ellipse 180px 160px at 500px 40px, var(--banner-peach) 0%, rgba(236,214,200,0) 100%),
      linear-gradient(90deg, #eef4f8 0%, #f4f6f8 55%, var(--banner-sand) 100%);
  }

  .banner-edge-fade {
    position: absolute;
    inset: 0;
    background:
      linear-gradient(90deg, rgba(156,198,230,0.45) 0%, rgba(156,198,230,0) 18%),
      linear-gradient(0deg, rgba(156,198,230,0.35) 0%, rgba(156,198,230,0) 22%);
  }

  .model-photo {
    position: absolute;
    left: 568px;
    top: 0;
    width: 384px;
    height: 396px;
    background:
      radial-gradient(ellipse 110px 140px at 220px 150px, var(--photo-skin) 0%, rgba(220,174,146,0) 100%),
      radial-gradient(ellipse 150px 110px at 230px 380px, var(--photo-sweater) 0%, rgba(236,232,227,0) 100%),
      radial-gradient(ellipse 170px 260px at 170px 190px, var(--photo-hair) 0%, rgba(74,54,44,0) 100%),
      linear-gradient(90deg, rgba(216,194,164,0) 0%, var(--banner-sand) 35%, #cdb79c 100%);
  }

  .headline {
    position: absolute;
    left: 114px;
    top: 100px;
    font-size: 29px;
    font-weight: 300;
    line-height: 39px;
    color: var(--headline-blue);
    letter-spacing: 0.1px;
  }

  .buy-button {
    position: absolute;
    left: 115px;
    top: 254px;
    width: 102px;
    height: 28px;
    border-radius: 14px;
    background: linear-gradient(180deg, var(--button-top), var(--button-bottom));
    box-shadow: 0 3px 5px rgba(20, 60, 110, 0.25);
    color: var(--button-text);
    font-size: 12px;
    line-height: 28px;
    text-align: center;
    text-decoration: none;
  }

  .product-placeholder {
    position: absolute;
    left: 446px;
    top: 97px;
    width: 112px;
    height: 192px;
  }
</style>
</head>
<body>
  <h1 class="board-label">Banner 4</h1>

  <section class="banner" aria-label="Home teeth whitening kits banner">
    <div class="banner-edge-fade" role="img" aria-label="Soft blurred background with blue fading squares at the edges"></div>
    <div class="model-photo" role="img" aria-label="Photo of a smiling woman with long dark hair and white teeth"></div>

    <h2 class="headline">The revolution in home<br>teeth whitening<br>is here</h2>

    <a class="buy-button" href="#">Buy Now</a>

    <svg class="product-placeholder" viewBox="0 0 112 192" aria-label="Space reserved for whitening kit product image">
      <polygon points="1,9 98,1 110,9 110,180 98,188 1,173" fill="var(--product-front)"/>
      <polygon points="98,1 110,9 110,180 98,188" fill="var(--product-side)"/>
    </svg>
  </section>
</body>
</html>
```